business card for law firm that reflects the web site -www.MarlaQuentby.com. That is pleasant to read

We need a business card for a small law firm. Your company designed our logo - tree of life - which I can provide to the designers. The card should be on both sides. Use the coloring from the web site (www.MarlaQuentby.com) and logo (I have several formats). I am attaching the logo, but not sure what format to use.

First side name of firm: Law Office of M.K. Quentby, P.A. 4819 West Pallisor, Suite 300, Phoenix, AZ 85016, Phone: 602.555.3841, Fax: 602.555.7290, web site: www.MarlaQuentby.com, email: MQuentby@MarlaQuentby.com.
Marla K. Quentby Bankruptcy and Foreclosure Attorney & Counselor.
Back side (perhaps vertical) the logo and then Notes with lines. At the bottom: Proud to help people and small businesses file for bankruptcy protection. We are a debt relief agency.
Updates

I have several versions of the logo. Will be happy to share whatever you need. Added Sunday, April 3, 2016

Target Market(s)

everyone

Industry/Entity Type

Legal

Contact Information for Business Card

I prefer something unique (rounded edges, design that adopts my web site - www.MarlaQuentby.com.

Font styles to use
Serif

Requirements
Must have
• First side name of firm: Law Office of M.K. Quentby, P.A. 4819 West Pallisor, Suite 300, Phoenix, AZ 85016, Phone: 602.555.3841, Fax: 602.555.7290, web site: www.MarlaQuentby.com, email: MQuentby@MarlaQuentby.com.
• Marla K. Quentby Bankruptcy and Foreclosure Attorney & Counselor.
• Back side (perhaps vertical) the logo and then Notes with lines. At the bottom: Proud to help people and small businesses file for bankruptcy protection. We are a debt relief agency.
• Green and brown colors that reflect the web site: www.MarlaQuentby.com
Should not have
• Type so small that older people cannot read.

```html
<!DOCTYPE html>
<html lang="en">
<head>
<meta charset="utf-8">
<title>Law Office of M.K. Quentby, P.A. — Business Card</title>
<link rel="stylesheet" href="https://fonts.googleapis.com/css2?family=Open+Sans:wght@400;600&display=swap">
<style>
  :root {
    --page-bg: #e9e6e3;
    --card-bg: #f8f6f4;
    --band-brown: #3b2213;
    --ring-white: #fbfaf8;
    --name-ink: #2b1a10;
    --title-green: #1e4a1c;
    --body-ink: #2a1d14;
    --icon-ink: #2b1a10;
    --contact-green: #1f4a1d;
  }
  * { box-sizing: border-box; margin: 0; padding: 0; }
  html, body {
    width: 1200px; height: 900px; overflow: hidden;
    background: var(--page-bg);
    font-family: "Open Sans", Arial, sans-serif;
  }
  .business-card {
    position: absolute; left: 161px; top: 178px;
    width: 878px; height: 543px;
    background: var(--card-bg);
    border-radius: 20px;
    overflow: hidden;
    box-shadow: 0 6px 24px rgba(60, 40, 25, 0.12);
  }
  .brand-band {
    position: absolute; left: 54px; top: 0;
    width: 173px; height: 100%;
    background: var(--band-brown);
  }
  .brand-seal {
    position: absolute; left: 20px; top: 162px;
    width: 222px; height: 222px;
    border-radius: 50%;
    background: var(--ring-white);
    display: flex; align-items: center; justify-content: center;
    text-align: center;
  }
  .brand-seal-name {
    font-size: 24px; font-weight: 600; line-height: 1.2;
    color: var(--band-brown);
  }
  .card-text { position: absolute; left: 301px; top: 0; right: 20px; }
  .line { position: absolute; left: 0; white-space: nowrap; }
  .attorney-name { top: 64px; font-size: 31px; font-weight: 600; color: var(--name-ink); }
  .attorney-title { font-size: 21px; color: var(--title-green); }
  .attorney-title.first { top: 102px; }
  .attorney-title.second { top: 135px; }
  .firm-name { top: 192px; font-size: 25px; font-weight: 600; color: var(--name-ink); }
  .firm-address { font-size: 22px; color: var(--body-ink); }
  .firm-address.first { top: 232px; }
  .firm-address.second { top: 270px; }
  .contact-list { list-style: none; }
  .contact-item {
    position: absolute; left: 14px;
    display: flex; align-items: center; gap: 16px;
    font-size: 21px; color: var(--contact-green);
  }
  .contact-item svg { width: 16px; height: 16px; fill: var(--icon-ink); flex: none; }
  .contact-phone { top: 331px; }
  .contact-fax { top: 367px; }
  .contact-web { top: 405px; }
  .contact-email { top: 441px; }
</style>
</head>
<body>
  <article class="business-card">
    <div class="brand-band"></div>
    <div class="brand-seal">
      <span class="brand-seal-name">M.K.<br>Quentby</span>
    </div>

    <section class="card-text">
      <h1 class="line attorney-name">Marla K. Quentby</h1>
      <p class="line attorney-title first">Bankruptcy and Foreclosure</p>
      <p class="line attorney-title second">Attorney &amp; Counselor</p>

      <h2 class="line firm-name">Law Office of M.K. Quentby</h2>
      <p class="line firm-address first">P.A. 4819 West Pallisor,</p>
      <p class="line firm-address second">Suite 300, Phoenix, AZ 85016</p>

      <ul class="contact-list">
        <li class="contact-item contact-phone">
          <svg viewBox="0 0 16 16" aria-hidden="true"><path d="M3.2 1l2.4 2.9-1.3 1.8c.9 2 2.5 3.6 4.5 4.5l1.8-1.3L13.6 11.3 12.4 14C6.5 13.7 2.3 9.5 2 3.6z"/></svg>
          <span>602.555.3841</span>
        </li>
        <li class="contact-item contact-fax">
          <svg viewBox="0 0 16 16" aria-hidden="true"><path d="M1 5h3v10H1zM5 3h7l2 2v10H5zm2 4v2h2V7zm3 0v2h2V7zm-3 3v2h2v-2zm3 0v2h2v-2z"/></svg>
          <span>602.555.7290</span>
        </li>
        <li class="contact-item contact-web">
          <svg viewBox="0 0 16 16" aria-hidden="true"><path d="M1 3h14v10H1zm1.5 1.3v.3L8 8.7l5.5-4.1v-.3zm0 1.9v5.5h11V6.2L8 10.3z"/></svg>
          <span>www.MarlaQuentby.com</span>
        </li>
        <li class="contact-item contact-email">
          <svg viewBox="0 0 16 16" aria-hidden="true"><circle cx="8" cy="8" r="7"/><path d="M5 4.5l2 1.5-.5 2L8 9.5 7.5 12 9.5 10l1-2 1.5-.5L11 5 9 4z" fill="#f8f6f4"/></svg>
          <span>MQuentby@MarlaQuentby.com</span>
        </li>
      </ul>
    </section>
  </article>
</body>
</html>
```